Generative AI radar Infographics

I want to create an infographic called "Automated Reasoning Horizon Chart for Tender Replies". (see slide 3 of the PowerPoint file). I want to use it on social media (Pellocast and Website). I added 2 inspiration graphics in my brief (see slide 2 of the PowerPoint). I want to add my logo on the infographic. (I also uploaded my company logos). You can find model detailed instructions on slide 1 of the PowerPoint.
Target Market(s)
Business development and sales
Industry/Entity Type
I am a business consultant. I will be using this infographics on Pellocast and in my powerpoint presentations to clients
Look and feel
Each slider illustrates characteristics of the customer's brand and the style your logo design should communicate.

```html
<!DOCTYPE html>
<html lang="en">
<head>
<meta charset="utf-8">
<title>Automated Reasoning Horizon Chart for Tender Replies</title>
<link href="https://fonts.googleapis.com/css2?family=Cinzel:wght@400&family=Montserrat:wght@400;800&family=Arimo:wght@700&display=swap" rel="stylesheet">
<style>
  :root{
    --navy:#0c2a3f;
    --blue:#0a8fbe;
    --white:#ffffff;
    --sky-top:#ffffff;
    --sky-mid:#c4e9f7;
    --sky-low:#62c0e2;
    --sky-base:#1590bd;
  }
  html,body{margin:0;padding:0;overflow:hidden;}
  body{width:1200px;height:778px;}
  .canvas{
    position:relative;width:1200px;height:778px;overflow:hidden;
    background:linear-gradient(180deg,var(--sky-top) 0%,var(--sky-top) 28%,var(--sky-mid) 52%,var(--sky-low) 80%,var(--sky-base) 100%);
    font-family:"Montserrat",Arial,sans-serif;color:var(--navy);
  }
  .brand{position:absolute;left:68px;top:98px;width:382px;
    font-family:"Montserrat",Arial,sans-serif;font-weight:800;font-size:23px;line-height:28px;
    letter-spacing:.5px;color:var(--navy);white-space:nowrap;}
  .axis-label{position:absolute;text-align:center;font-weight:800;font-size:21px;line-height:24px;letter-spacing:.5px;}
  .axis-label .note{display:block;font-weight:400;font-size:13.5px;line-height:16px;letter-spacing:.3px;margin-top:2px;}
  .axis-top{left:562px;top:38px;width:300px;}
  .axis-bottom{left:566px;top:704px;width:300px;}
  .axis-left{left:163px;top:357px;width:300px;}
  .axis-right{left:955px;top:357px;width:300px;}
  .chart-title{position:absolute;left:46px;top:598px;margin:0;font-weight:800;font-size:33px;line-height:42px;letter-spacing:.5px;color:var(--navy);text-transform:uppercase;}
  .radar{position:absolute;left:0;top:0;}
  .band-title{font-family:"Cinzel",Georgia,serif;font-weight:400;font-size:27px;fill:var(--white);}
  .item{font-family:"Arimo",Arial,sans-serif;font-weight:700;font-size:9.5px;fill:var(--white);}
  .hub-name{font-family:"Montserrat",Arial,sans-serif;font-weight:800;font-size:19px;fill:var(--navy);}
</style>
</head>
<body>
<div class="canvas">

  <div class="brand">CALVERIN ADVISORY GROUP</div>

  <svg class="radar" width="1200" height="778" viewBox="0 0 1200 778" aria-label="Horizon chart with four quadrants">
    <defs>
      <linearGradient id="fill-decision" x1="0" y1="1" x2="1" y2="0"><stop offset="0" stop-color="#1c1c1d"/><stop offset="1" stop-color="#4b4b4d"/></linearGradient>
      <linearGradient id="fill-development" x1="0" y1="0" x2="1" y2="1"><stop offset="0" stop-color="#69696c"/><stop offset="1" stop-color="#8a8a8d"/></linearGradient>
      <linearGradient id="fill-proposal" x1="0" y1="0" x2="1" y2="1"><stop offset="0" stop-color="#262627"/><stop offset="1" stop-color="#4a4a4b"/></linearGradient>
      <linearGradient id="fill-capture" x1="0" y1="0" x2="1" y2="1"><stop offset="0" stop-color="#85858a"/><stop offset="1" stop-color="#5f5f62"/></linearGradient>

      <path id="arc-decision-title" d="M471,387 A243,243 0 0 1 714,144"/>
      <path id="arc-development-title" d="M714,144 A243,243 0 0 1 957,387"/>
      <path id="arc-proposal-title" d="M714,659 A272,272 0 0 0 986,387"/>
      <path id="arc-capture-title" d="M442,387 A272,272 0 0 0 714,659"/>

      <path id="tl1" d="M514,387 A200,200 0 0 1 714,187"/>
      <path id="tl2" d="M531,387 A183,183 0 0 1 714,204"/>
      <path id="tl3" d="M548,387 A166,166 0 0 1 714,221"/>
      <path id="tl4" d="M565,387 A149,149 0 0 1 714,238"/>
      <path id="tl5" d="M582,387 A132,132 0 0 1 714,255"/>
      <path id="tl6" d="M599,387 A115,115 0 0 1 714,272"/>

      <path id="tr1" d="M714,184 A203,203 0 0 1 917,387"/>
      <path id="tr2" d="M714,201 A186,186 0 0 1 900,387"/>
      <path id="tr3" d="M714,218 A169,169 0 0 1 883,387"/>
      <path id="tr4" d="M714,235 A152,152 0 0 1 866,387"/>
      <path id="tr5" d="M714,252 A135,135 0 0 1 849,387"/>
      <path id="tr6" d="M714,269 A118,118 0 0 1 832,387"/>

      <path id="br1" d="M714,504 A117,117 0 0 0 831,387"/>
      <path id="br2" d="M714,521 A134,134 0 0 0 848,387"/>
      <path id="br3" d="M714,538 A151,151 0 0 0 865,387"/>
      <path id="br4" d="M714,555 A168,168 0 0 0 882,387"/>
      <path id="br5" d="M714,572 A185,185 0 0 0 899,387"/>

      <path id="bl1" d="M597,387 A117,117 0 0 0 714,504"/>
      <path id="bl2" d="M580,387 A134,134 0 0 0 714,521"/>
      <path id="bl3" d="M563,387 A151,151 0 0 0 714,538"/>
      <path id="bl4" d="M546,387 A168,168 0 0 0 714,555"/>
      <path id="bl5" d="M529,387 A185,185 0 0 0 714,572"/>
      <path id="bl6" d="M512,387 A202,202 0 0 0 714,589"/>
    </defs>

    <!-- outer ring and bands -->
    <circle class="ring-outer" cx="714" cy="387" r="292" fill="var(--navy)"/>
    <path class="band band-development" d="M714,387 L714,102 A285,285 0 0 1 999,387 Z" fill="var(--blue)"/>
    <path class="band band-capture" d="M714,387 L429,387 A285,285 0 0 0 714,672 Z" fill="var(--blue)"/>
    <circle class="ring-inner" cx="714" cy="387" r="233" fill="var(--blue)"/>

    <!-- quadrants -->
    <path class="quadrant" d="M714,387 L486,387 A228,228 0 0 1 714,159 Z" fill="url(#fill-decision)"/>
    <path class="quadrant" d="M714,387 L714,159 A228,228 0 0 1 942,387 Z" fill="url(#fill-development)"/>
    <path class="quadrant" d="M714,387 L942,387 A228,228 0 0 1 714,615 Z" fill="url(#fill-proposal)"/>
    <path class="quadrant" d="M714,387 L714,615 A228,228 0 0 1 486,387 Z" fill="url(#fill-capture)"/>

    <!-- direction arrows -->
    <polygon class="arrow" points="713,122 692,161 734,161" fill="var(--white)"/>
    <polygon class="arrow" points="971,382 932,360 932,404" fill="var(--white)"/>
    <polygon class="arrow" points="712,639 691,601 733,601" fill="var(--white)"/>
    <polygon class="arrow" points="454,382 493,360 493,404" fill="var(--white)"/>

    <!-- band titles -->
    <text class="band-title" text-anchor="middle"><textPath href="#arc-decision-title" startOffset="50%" textLength="268" lengthAdjust="spacingAndGlyphs">DECISION SUPPORT</textPath></text>
    <text class="band-title" text-anchor="middle"><textPath href="#arc-development-title" startOffset="50%" textLength="350" lengthAdjust="spacingAndGlyphs">PROPOSAL DEVELOPMENT</textPath></text>
    <text class="band-title" text-anchor="middle"><textPath href="#arc-proposal-title" startOffset="50%" textLength="295" lengthAdjust="spacingAndGlyphs">PROPOSAL STRATEGY</textPath></text>
    <text class="band-title" text-anchor="middle"><textPath href="#arc-capture-title" startOffset="50%" textLength="286" lengthAdjust="spacingAndGlyphs">CAPTURE STRATEGY</textPath></text>

    <!-- decision support items -->
    <g class="items" text-anchor="middle">
      <text class="item"><textPath href="#tl1" startOffset="50%">. BID/NO BID ANALYSIS</textPath></text>
      <text class="item"><textPath href="#tl2" startOffset="50%">. STRATEGIC PRICING OPTIMIZATION</textPath></text>
      <text class="item"><textPath href="#tl3" startOffset="50%">. OPPORTUNITY ASSESSMENT</textPath></text>
      <text class="item"><textPath href="#tl4" startOffset="50%">. WIN PROBABILITY MODELING</textPath></text>
      <text class="item"><textPath href="#tl5" startOffset="50%">. BID QUALIFICATION</textPath></text>
      <text class="item"><textPath href="#tl6" startOffset="50%">. COMPLIANCE ASSESSMENT</textPath></text>
    </g>

    <!-- proposal development items -->
    <g class="items" text-anchor="middle">
      <text class="item"><textPath href="#tr1" startOffset="50%">. COMPANY PROFILE . CV AND RESUMES</textPath></text>
      <text class="item"><textPath href="#tr2" startOffset="50%">. PAST PERFORMANCES . TECHNICAL SOLUTIONS</textPath></text>
      <text class="item"><textPath href="#tr3" startOffset="50%">. COMPLIANCE MATRIX . STATEMENT OF WORK</textPath></text>
      <text class="item"><textPath href="#tr4" startOffset="50%">. DUE DILIGENCE QUESTIONNAIRES</textPath></text>
      <text class="item"><textPath href="#tr5" startOffset="50%">. EXECUTIVE SUMMARY</textPath></text>
      <text class="item"><textPath href="#tr6" startOffset="50%">. SECURITY QUESTIONNAIRES</textPath></text>
    </g>

    <!-- proposal strategy items -->
    <g class="items" text-anchor="middle">
      <text class="item"><textPath href="#br1" startOffset="50%">. PROPOSAL PLAN</textPath></text>
      <text class="item"><textPath href="#br2" startOffset="50%">. PROPOSAL OUTLINE</textPath></text>
      <text class="item"><textPath href="#br3" startOffset="50%">. DIFFERENTIATORS</textPath></text>
      <text class="item"><textPath href="#br4" startOffset="50%">. WIN THEME EXTRACTION</textPath></text>
      <text class="item"><textPath href="#br5" startOffset="50%">. KEY MESSAGES EXTRACTION</textPath></text>
    </g>

    <!-- capture strategy items -->
    <g class="items" text-anchor="middle">
      <text class="item"><textPath href="#bl1" startOffset="50%">. CAPTURE PLAN</textPath></text>
      <text class="item"><textPath href="#bl2" startOffset="50%">. SWOT ANALYSIS</textPath></text>
      <text class="item"><textPath href="#bl3" startOffset="50%">. CUSTOMER HOT BUTTONS</textPath></text>
      <text class="item"><textPath href="#bl4" startOffset="50%">. CUSTOMER INTELLIGENCE</textPath></text>
      <text class="item"><textPath href="#bl5" startOffset="50%">. COMPETITIVE INTELLIGENCE</textPath></text>
      <text class="item"><textPath href="#bl6" startOffset="50%">. VALUE PROPOSITION</textPath></text>
    </g>

    <!-- hub -->
    <circle class="hub" cx="714" cy="387" r="88" fill="var(--white)"/>
    <text class="hub-name" x="714" y="394" text-anchor="middle">CALVERIN</text>
  </svg>

  <div class="axis-label axis-top">PROCESS<br>ENHANCEMENT</div>
  <div class="axis-label axis-left">INSIGHTS<br>GENERATION<span class="note">(Transformative<br>Application)</span></div>
  <div class="axis-label axis-right">TASK<br>AUTOMATION<span class="note">(Foundational Use)</span></div>
  <div class="axis-label axis-bottom">STRATEGY<br>ENABLEMENT</div>

  <h1 class="chart-title">Automated Reasoning<br>Horizon Chart for<br>Tender Replies</h1>
</div>
</body>
</html>
```